Hop Onward Flyer

Marketing Promo Flyer

***I uploaded the 2022 version just as an example. I'm open to NEW designs!

Brookvane 50th Anniversary Logo
ALL ONWARD
New customers receive up to $3,000 toward your orders!

HOP ONWARD
Buy $10,000 Receive $500
Buy $25,000 Receive $500
Buy $50,000 Receive $500
Buy $200,000 Receive $500

KEEP ONWARD
Complete all levels of Hop Onward then the following year spend the same or more as previous year and get $1,000!

Terms and conditions: A new customer is a contactor that has purchased less than $2,000 with Brookvane Supply in the past six (6) months from the time of the first eligible voucher. Materials must be paid. The customer has 12 months from the date of the first qualifying purchase to reach all levels of Hop onward. If you reach all four levels of Hop Onward, you are then eligible for Keep Onward. Keep Onward voucher may be rewarded when you match or beat the previous year purchase. The vouchers are to be used toward future purchases but may not be used to pay off previous balance on the customer's account. No one-time purchasers. This promotion and your participation in it is void where prohibited by law, rules or regulations. Brookvane Supply reserves the right to cancel, suspend, and/or modify this promotion at any time, for any reason, without prior notice. Vouchers are valid up to one year after issued date. Promotion expires December 31, 2023. All rights reserved by Brookvane Supply.

```html
<!DOCTYPE html>
<html lang="en">
<head>
<meta charset="utf-8">
<title>Hop Onward Flyer</title>
<link href="https://fonts.googleapis.com/css2?family=Montserrat:wght@300;400;500;600;700&display=swap" rel="stylesheet">
<style>
  :root {
    --navy: #1b2a8c;
    --blue: #2458b8;
    --blue-deep: #1c47a3;
    --blue-text: #1f6fc4;
    --orange: #f29a1f;
    --orange-light: #f7b23a;
    --ink: #151515;
    --white: #ffffff;
    --grey-light: #ececec;
    --grey-mid: #cfcfcf;
    --terms-bg: #454545;
    --terms-text: #f0f0f0;
    --water: #39a6d6;
    --water-deep: #1a7fb8;
  }
  * { margin: 0; padding: 0; box-sizing: border-box; }
  html, body { width: 892px; height: 1200px; overflow: hidden; background: var(--white); }
  body { font-family: "Montserrat", Arial, sans-serif; color: var(--ink); }
  .flyer { position: relative; width: 892px; height: 1200px; overflow: hidden; background: var(--white); }

  .top-swoosh { position: absolute; left: 0; top: 0; width: 892px; height: 260px; }

  .brand-mark {
    position: absolute; left: 560px; top: 48px; width: 270px; height: 140px;
    display: flex; align-items: center; justify-content: center; gap: 12px;
  }
  .brand-mark .dot { width: 18px; height: 18px; border-radius: 50%; background: var(--navy); flex: none; }
  .brand-mark .name {
    font-weight: 700; color: var(--navy); font-size: 24px; line-height: 1.15; text-align: center;
  }

  .offer-band {
    position: absolute; left: 0; top: 214px; width: 892px; height: 245px;
    background: linear-gradient(90deg, var(--white) 40%, #f4f4f4 100%);
  }

  .photo-boat {
    position: absolute; left: -22px; top: 40px; width: 460px; height: 470px; border-radius: 50%;
    background: linear-gradient(180deg, #f3f3f3 0%, #d9d9d9 48%, #3fb0dc 58%, #1b88c2 100%);
    border: 6px solid var(--white);
  }

  .headline-all {
    position: absolute; left: 456px; top: 244px; font-size: 56px; letter-spacing: -1.5px; color: var(--navy);
    line-height: 1;
  }
  .headline-all .light { font-weight: 300; }
  .headline-all .bold { font-weight: 700; }

  .offer-ribbon {
    position: absolute; left: 428px; top: 316px; width: 450px; height: 43px;
    background: linear-gradient(90deg, var(--orange-light), var(--orange));
    clip-path: polygon(0 0, 100% 0, 96% 100%, 0 100%);
    color: var(--ink); font-size: 25px; font-weight: 500; line-height: 43px; padding-left: 18px;
  }

  .offer-amount { position: absolute; left: 440px; top: 368px; display: flex; align-items: center; gap: 16px; color: var(--navy); }
  .offer-amount .sum { font-size: 70px; font-weight: 600; letter-spacing: -2px; line-height: 1; }
  .offer-amount .note { font-size: 30px; font-weight: 400; line-height: 0.95; letter-spacing: -0.5px; }

  .levels {
    position: absolute; left: 0; top: 459px; width: 892px; height: 346px;
    background: linear-gradient(90deg, #2d6cc9 0%, var(--blue) 50%, var(--blue-deep) 100%);
  }

  .photo-jump {
    position: absolute; left: 26px; top: 492px; width: 340px; height: 340px; border-radius: 50%;
    background: radial-gradient(circle at 40% 40%, #8cc4ec 0%, #5aa4e0 60%, #3b88d0 100%);
    border: 5px solid var(--white); box-shadow: 0 0 0 3px var(--blue-deep);
  }

  .levels-title-top { position: absolute; left: 402px; top: 492px; font-size: 46px; font-weight: 300; color: var(--white); line-height: 1; }
  .levels-title-bar {
    position: absolute; left: 310px; top: 549px; width: 345px; height: 52px; background: var(--white);
    clip-path: polygon(0 0, 93% 0, 100% 100%, 0 100%);
  }
  .levels-title-bottom { position: absolute; left: 402px; top: 553px; font-size: 44px; font-weight: 700; color: var(--blue-text); line-height: 1; letter-spacing: -0.5px; }

  .level-list { position: absolute; left: 404px; top: 624px; list-style: none; }
  .level-list li { display: flex; align-items: center; gap: 10px; height: 39px; color: var(--white); font-size: 29px; font-weight: 300; letter-spacing: -0.6px; }
  .level-list .tick { width: 28px; height: 28px; flex: none; }
  .level-list b { font-weight: 700; }
  .level-list .reward { color: var(--orange-light); font-weight: 700; }

  .retain { position: absolute; left: 0; top: 805px; width: 892px; height: 242px; background: var(--white); }
  .photo-island {
    position: absolute; left: 600px; top: 835px; width: 292px; height: 160px;
    background: radial-gradient(ellipse at 65% 45%, #3f6b2a 0%, #7d9a4a 35%, rgba(200,220,200,0.3) 65%, rgba(255,255,255,0) 80%);
  }
  .water-band {
    position: absolute; left: 0; top: 950px; width: 892px; height: 97px;
    background: linear-gradient(180deg, rgba(255,255,255,0) 0%, #bfe6f4 22%, #63bfe4 50%, var(--water) 75%, var(--water-deep) 100%);
  }
  .retain-title { position: absolute; left: 33px; top: 852px; font-size: 58px; letter-spacing: -2px; line-height: 1; color: var(--ink); }
  .retain-title .light { font-weight: 400; }
  .retain-title .bold { font-weight: 700; color: var(--blue-text); }
  .retain-copy { position: absolute; left: 33px; top: 918px; width: 600px; font-size: 19.5px; line-height: 1.25; font-weight: 400; color: var(--ink); }
  .retain-copy b { font-weight: 700; }

  .terms {
    position: absolute; left: 0; top: 1047px; width: 892px; height: 153px; background: var(--terms-bg);
    padding: 18px 33px 0 33px; color: var(--terms-text); font-size: 11.2px; line-height: 13.4px; font-weight: 400;
  }
  .terms b { font-weight: 700; }
</style>
</head>
<body>
<div class="flyer">
  <svg class="top-swoosh" viewBox="0 0 892 260" aria-hidden="true">
    <defs>
      <linearGradient id="swooshGrey" x1="0" y1="0" x2="0" y2="1">
        <stop offset="0" stop-color="#ffffff"/>
        <stop offset="1" stop-color="#d4d4d4"/>
      </linearGradient>
    </defs>
    <path d="M380 140 C520 215 700 230 892 205 L892 260 L380 260 Z" fill="url(#swooshGrey)"/>
  </svg>

  <div class="brand-mark">
    <span class="dot"></span>
    <span class="name">Brookvane<br>50th Anniversary</span>
  </div>

  <div class="offer-band"></div>

  <div class="photo-boat" role="img" aria-label="Paper boat folded from a banknote floating on blue ocean water"></div>

  <h1 class="headline-all"><span class="light">ALL </span><span class="bold">ONWARD</span></h1>
  <div class="offer-ribbon">New customers receive up to</div>
  <div class="offer-amount">
    <span class="sum">$3,000</span>
    <span class="note">toward your<br>orders!</span>
  </div>

  <section class="levels"></section>
  <div class="photo-jump" role="img" aria-label="Person in a jacket leaping forward against a blue sky"></div>

  <h2 class="levels-title-top">HOP</h2>
  <div class="levels-title-bar"></div>
  <h2 class="levels-title-bottom">ONWARD</h2>

  <ul class="level-list">
    <li><svg class="tick" viewBox="0 0 28 28" aria-hidden="true"><circle cx="14" cy="14" r="13" fill="#f7b23a"/><path d="M8 14.5 L12.5 19 L20 10" fill="none" stroke="#fff" stroke-width="3" stroke-linecap="round" stroke-linejoin="round"/></svg><span><b>Buy</b> $10,000 Receive <span class="reward">$500</span></span></li>
    <li><svg class="tick" viewBox="0 0 28 28" aria-hidden="true"><circle cx="14" cy="14" r="13" fill="#f7b23a"/><path d="M8 14.5 L12.5 19 L20 10" fill="none" stroke="#fff" stroke-width="3" stroke-linecap="round" stroke-linejoin="round"/></svg><span><b>Buy</b> $25,000 Receive <span class="reward">$500</span></span></li>
    <li><svg class="tick" viewBox="0 0 28 28" aria-hidden="true"><circle cx="14" cy="14" r="13" fill="#f7b23a"/><path d="M8 14.5 L12.5 19 L20 10" fill="none" stroke="#fff" stroke-width="3" stroke-linecap="round" stroke-linejoin="round"/></svg><span><b>Buy</b> $50,000 Receive <span class="reward">$500</span></span></li>
    <li><svg class="tick" viewBox="0 0 28 28" aria-hidden="true"><circle cx="14" cy="14" r="13" fill="#f7b23a"/><path d="M8 14.5 L12.5 19 L20 10" fill="none" stroke="#fff" stroke-width="3" stroke-linecap="round" stroke-linejoin="round"/></svg><span><b>Buy</b> $200,000 Receive <span class="reward">$500</span></span></li>
  </ul>

  <section class="retain"></section>
  <div class="photo-island" role="img" aria-label="Tropical island with palm trees and a sandy beach"></div>
  <div class="water-band" role="img" aria-label="Clear turquoise sea surface"></div>
  <h2 class="retain-title"><span class="light">KEEP </span><span class="bold">ONWARD</span></h2>
  <p class="retain-copy">Complete all levels of Hop Onward then the following year spend the same or more as previous year and get <b>$1,000!</b></p>

  <footer class="terms">
    <p><b>Terms and conditions:</b> A new customer is a contactor that has purchased less than $2,000 with Brookvane Supply in the past six (6) months from the time of the first eligible voucher. Materials must be paid. The customer has 12 months from the date of the first qualifying purchase to reach all levels of Hop onward. If you reach all four levels of Hop Onward, you are then eligible for Keep Onward. Keep Onward voucher may be rewarded when you match or beat the previous year purchase. The vouchers are to be used toward future purchases but may not be used to pay off previous balance on the customer's account. No one-time purchasers. This promotion and your participation in it is void where prohibited by law, rules or regulations. Brookvane Supply reserves the right to cancel, suspend, and/or modify this promotion at any time, for any reason, without prior notice. Vouchers are valid up to one year after issued date. Promotion expires December 31, 2023. All rights reserved by Brookvane Supply.</p>
  </footer>
</div>
</body>
</html>
```